Pick Our Rooftop lead generation web-site.

A Multi-purpose lead generation site with unique selling proposition, hero shot, benefits, social proof, and call-to-action. looking for a clean, modern site that is scalable. The site should be search engine optimized.
Updates

Reason: Will be reviewing designs submitted and ask for changes if any.

Target Market(s)

Homeowner and automobile owners that also own busineses.

Industry/Entity Type

Insurance

Coding

Coded - Design and coding required

Number of Pages Required

5+ page

Font styles to use
Serif

Requirements
Must have
• Optimization for mobile devices, a clean site similar to (https://shieldbramble.com), Easy to use, Interactivity, and easy content management. Quote forms for personal and commercial auto, homeowners, business owners insurance. Adroll on pages (analytics)
Nice to have
• Uses of Technology similar to https://protavo.com. Integration or ability to push to third-party tools. Auto email responses, Chat integration, social media (join our group, sign up RSS feeds).
Should not have
• Links that closes our site.

```html
<!DOCTYPE html>
<html lang="en">
<head>
<meta charset="utf-8">
<title>Pick Our Rooftop — Home Insurance Quotes</title>
<link rel="stylesheet" href="https://fonts.googleapis.com/css2?family=Raleway:wght@500;600;700&family=Open+Sans:ital,wght@0,400;0,600;0,700;1,400&display=swap">
<style>
:root{
  --blue:#0a73b8;
  --blue-band:#0d87cc;
  --ink:#222;
  --text:#3a3a3a;
  --muted:#666;
  --grey-bg:#ececec;
  --field:#ececec;
  --footer:#343536;
  --footer-text:#cfcfcf;
  --star:#f39c12;
  --white:#fff;
}
*{box-sizing:border-box;margin:0;padding:0}
html,body{width:1200px;height:2293px;overflow:hidden}
body{position:relative;background:var(--white);font-family:"Open Sans",Arial,sans-serif;color:var(--text)}
h1,h2,h3,.nav,.btn,.brand{font-family:"Raleway","Open Sans",sans-serif}
.section{position:absolute;left:0;width:1200px}

/* header */
.site-header{top:0;height:92px;background:var(--white)}
.brand{position:absolute;left:160px;top:28px;display:flex;align-items:center;gap:10px;font-size:24px;font-weight:600;color:var(--blue)}
.brand-dot{width:36px;height:36px;border-radius:50%;background:var(--blue)}
.nav{position:absolute;left:463px;top:0;height:92px;display:flex;align-items:center;font-size:12px;font-weight:700;color:var(--ink);letter-spacing:.3px}
.nav a{color:inherit;text-decoration:none;margin-right:32px}
.nav .phone{border-left:1px solid #ddd;padding-left:16px;height:30px;display:flex;align-items:center;font-size:15px;font-weight:600;color:#444;margin-left:-12px}

/* hero */
.hero{top:92px;height:513px;background:linear-gradient(110deg,#e7e4dc 0%,#b9b2a6 35%,#7d756c 55%,#d9d5cd 75%,#9a948d 100%)}
.contact-card{position:absolute;left:703px;top:134px;width:335px;height:248px;background:var(--white);border-top:8px solid var(--blue);padding:16px 26px 0}
.contact-card h2{text-align:center;font-size:19px;font-weight:600;color:#333;margin-bottom:12px}
.field{display:block;height:37px;background:var(--field);border:1px solid #dcdcdc;margin-bottom:6px;padding:0 12px;line-height:35px;font-size:11px;font-style:italic;color:#555}
.btn{display:inline-block;background:var(--blue);color:var(--white);font-weight:700;font-size:12.5px;letter-spacing:.4px;text-align:center}
.contact-card .btn{width:100px;height:36px;line-height:36px;margin-top:3px}
.dots{position:absolute;left:561px;top:455px;display:flex;gap:8px}
.dots span{width:15px;height:15px;border-radius:50%;background:var(--white)}
.dots span.on{background:var(--blue);border:2px solid var(--white)}

/* welcome */
.welcome{top:605px;height:309px;text-align:center}
.welcome h1{margin-top:37px;font-size:26px;font-weight:600;color:var(--ink)}
.welcome h1 span{color:var(--blue)}
.welcome p{width:756px;margin:22px auto 0;font-size:10.5px;line-height:19.6px;color:var(--text)}
.welcome .btn{margin-top:26px;width:166px;height:37px;line-height:37px}

/* benefits & features */
.perks{top:914px;height:496px;background:var(--grey-bg)}
.perk-col{position:absolute;top:48px;width:390px}
.perk-col.left{left:160px}
.perk-col.right{left:654px}
.perks .divider{position:absolute;left:600px;top:92px;width:1px;height:330px;background:#d2d2d2}
.perk-col h2{font-size:24px;font-weight:500;color:var(--ink);margin-bottom:27px}
.perk{display:flex;gap:15px;height:124px}
.perk-icon{flex:none;width:46px;height:46px;border-radius:50%;border:1.5px solid #444;display:flex;align-items:center;justify-content:center;margin-top:4px}
.perk-icon.accent{border-color:var(--blue)}
.perk h3{font-size:17px;font-weight:500;color:var(--ink);margin-bottom:7px}
.perk h3.accent{color:var(--blue)}
.perk p{font-size:10.5px;line-height:18px;color:var(--text);width:328px}

/* testimonials */
.testimonials{top:1410px;height:329px}
.testimonials h2{text-align:center;margin-top:46px;font-size:24px;font-weight:600;color:var(--ink)}
.quote{position:absolute;top:119px;display:flex;gap:26px}
.quote.one{left:159px}
.quote.two{left:613px}
.portrait{width:142px;height:142px;border-radius:50%}
.portrait.a{background:radial-gradient(circle at 50% 40%,#cfc9c1,#6f6a64 70%,#3e3b38)}
.portrait.b{background:radial-gradient(circle at 50% 40%,#d8c2ae,#8a6a52 70%,#5e4535)}
.quote blockquote{width:260px;margin-top:10px;font-size:10.5px;line-height:19.5px;color:var(--text)}
.quote cite{display:block;margin-top:11px;font-style:normal;font-weight:600;font-size:11.5px;color:var(--blue)}

/* newsletter */
.newsletter{top:1739px;height:100px;background:var(--blue-band)}
.news-mark{position:absolute;left:163px;top:26px;width:48px;height:48px;border-radius:50%;border:3px solid var(--white)}
.newsletter h2{position:absolute;left:245px;top:32px;font-size:17px;line-height:19px;font-weight:700;color:var(--white);letter-spacing:.5px}
.news-field{position:absolute;top:31px;height:39px;background:var(--white);padding-left:12px;line-height:39px;font-size:11.5px;color:#222}
.news-field.name{left:382px;width:266px}
.news-field.email{left:657px;width:280px}
.newsletter .signup{position:absolute;left:946px;top:31px;width:92px;height:39px;line-height:39px;background:#0b0b0b}

/* reviews */
.reviews{top:1839px;height:216px}
.review{position:absolute;top:42px;width:420px}
.review.one{left:160px}
.review.two{left:634px}
.review h3{display:flex;align-items:center;gap:10px;font-size:13px;font-weight:700;letter-spacing:1.5px;color:var(--ink)}
.review h3 .src{font-size:15px;letter-spacing:0;color:#333}
.review h3 .badge{width:14px;height:14px;border-radius:50%;background:#888}
.review p{margin-top:18px;font-size:10px;line-height:19.5px;font-style:italic;color:#333}
.review .by{margin-top:12px;display:flex;align-items:center;gap:12px;font-size:12px;color:#444}

/* footer */
.site-footer{top:2055px;height:238px;background:var(--footer);color:var(--footer-text)}
.footer-top{position:absolute;left:160px;top:24px;width:878px;height:43px;border-bottom:1px solid #4a4b4c;display:flex;justify-content:space-between;font-size:11px;color:#e6e6e6}
.footer-top .social{display:flex;gap:4px;margin-top:-8px}
.footer-top .social span{width:24px;height:24px;border-radius:50%;border:1.5px solid var(--white);background:#6b8fb0}
.disclaimer{position:absolute;left:160px;top:92px;width:880px;font-size:10px;line-height:19.5px;color:#bdbdbd}
.disclaimer b{color:var(--white)}
</style>
</head>
<body>

<header class="section site-header">
  <div class="brand"><span class="brand-dot"></span>PickOurRooftop.com</div>
  <nav class="nav">
    <a>HOME</a><a>SERVICES</a><a>TESTIMONIAL</a><a>FAQ'S</a><a>CONTACT</a><a>ABOUT</a>
    <span class="phone">888-555-0142</span>
  </nav>
</header>

<section class="section hero">
  <div role="img" aria-label="Smiling homeowner on the phone, sitting on a sofa in a bright living room" style="position:absolute;inset:0"></div>
  <form class="contact-card">
    <h2>CONTACT FORM</h2>
    <span class="field">Name:</span>
    <span class="field">Email:</span>
    <span class="field">Phone*:</span>
    <span class="btn">SUBMIT</span>
  </form>
  <div class="dots"><span></span><span class="on"></span><span></span><span></span></div>
</section>

<section class="section welcome">
  <h1>Welcome to Pick <span>Our Rooftop</span></h1>
  <p>Sed ut perspiciatis unde omnis iste natus error sit voluptatem accusantium doloremque laudantium, totam rem aperiam, eaque ipsa quae ab illoe audantium, totaminventorSed ut perspiciatis unde omnis iste natus error sit voluptatem accusantium doloremque laudantium, totam rem aperiam, eaqu ipsa quae ab illo e laudantium, totaminventore. Sed ut perspiciatis unde omnis iste natus error sit voluptatem accusantium doloremque laudantium, totam rem aperiam, eaque ipsa quae ab illo e laudantium, totaminventore. Sed ut perspiciatis unde omnis iste natus error sit voluptatem accusantium dolorem ue laudantium, totam rem aperiam, eaque ipsa quae ab illo e laudantium, totaminventore. Sed ut perspiciatis unde omnis iste natus error sit voluptatem cusantium doloremque lauda ntium, totam rem ap eriam, eaque ipsa quae ab illo e lalore udantium, totaminv lorem entore.</p>
  <span class="btn">MORE INFORMATION</span>
</section>

<section class="section perks">
  <div class="divider"></div>
  <div class="perk-col left">
    <h2>Benefits</h2>
    <div class="perk">
      <span class="perk-icon accent"><svg width="20" height="20" viewBox="0 0 20 20"><path d="M2 7h4l9-5v16l-9-5H2z" fill="none" stroke="var(--blue)" stroke-width="2"/><path d="M6 13l2 5" stroke="var(--blue)" stroke-width="2"/></svg></span>
      <div><h3 class="accent">Finibus Bonorum et Malorum</h3><p>Sed ut perspiciatis unde omnis iste natus error sit voluptatem acc usantium doloremque laudantium, totam rem aperiam, eaque ips a quae ab illo e laudantium, totaminventore.</p></div>
    </div>
    <div class="perk">
      <span class="perk-icon"><svg width="20" height="18" viewBox="0 0 20 18"><path d="M10 1L1 9h3v8h4v-5h4v5h4V9h3z" fill="#555"/></svg></span>
      <div><h3>Loris nisi ut aliquip ex ea commo</h3><p>Sed ut perspiciatis unde omnis iste natus error sit voluptatem acc usantium doloremque laudantium, totam rem aperiam, eaque ips a quae ab illo e laudantium, totaminventore.</p></div>
    </div>
    <div class="perk">
      <span class="perk-icon"><svg width="20" height="18" viewBox="0 0 20 18"><path d="M10 17L2 9a4.5 4.5 0 0 1 8-5 4.5 4.5 0 0 1 8 5z" fill="#555"/></svg></span>
      <div><h3>Perspiciatis unde omnis iste natus</h3><p>Sed ut perspiciatis unde omnis iste natus error sit voluptatem acc usantium doloremque laudantium, totam rem aperiam, eaque ips a quae ab illo e laudantium, totaminventore.</p></div>
    </div>
  </div>
  <div class="perk-col right">
    <h2>Features</h2>
    <div class="perk">
      <span class="perk-icon accent"><svg width="22" height="22" viewBox="0 0 22 22"><circle cx="11" cy="11" r="9" fill="none" stroke="var(--blue)" stroke-width="2"/><circle cx="11" cy="11" r="4" fill="none" stroke="var(--blue)" stroke-width="2"/><path d="M11 2v5M11 15v5M2 11h5M15 11h5" stroke="var(--blue)" stroke-width="2"/></svg></span>
      <div><h3 class="accent">Accusantium doloremque laudant</h3><p>Sed ut perspiciatis unde omnis iste natus error sit voluptatem acc usantium doloremque laudantium, totam rem aperiam, eaque ips a quae ab illo e laudantium, totaminventore.</p></div>
    </div>
    <div class="perk">
      <span class="perk-icon"><svg width="14" height="22" viewBox="0 0 14 22"><path d="M12 5.5C11 4 9.5 3.5 7 3.5S2 5 2 7s2 3 5 3.6 5 1.6 5 3.9-2 3.5-5 3.5-4.5-.8-5.5-2.3M7 1v20" fill="none" stroke="#555" stroke-width="1.8"/></svg></span>
      <div><h3>Sed quia consequuntur magn</h3><p>Sed ut perspiciatis unde omnis iste natus error sit voluptatem acc usantium doloremque laudantium, totam rem aperiam, eaque ips a quae ab illo e laudantium, totaminventore.</p></div>
    </div>
    <div class="perk">
      <span class="perk-icon"><svg width="22" height="18" viewBox="0 0 22 18"><rect x="1" y="1" width="20" height="12" rx="1" fill="none" stroke="#555" stroke-width="2"/><path d="M8 17h6M11 13v4" stroke="#555" stroke-width="2"/></svg></span>
      <div><h3>Sed quia consequunturgn</h3><p>Sed ut perspiciatis unde omnis iste natus error sit voluptatem acc usantium doloremque laudantium, totam rem aperiam, eaque ips a quae ab illo e laudantium, totaminventore.</p></div>
    </div>
  </div>
</section>

<section class="section testimonials">
  <h2>Testimonials</h2>
  <div class="quote one">
    <div class="portrait a" role="img" aria-label="Portrait photo of a satisfied male customer"></div>
    <blockquote>“ Sed ut perspiciatis unde omnlois iste natus error sit volup tatem accusantium doremue laudantium, to tam rem aperiam, eaque ipsa quae ab illo inventore veritatis etuasi architecto beatae vitae dicta sunt explicaboemo enim ipsam voluptatequi”<cite>Jhon Smith, City Name</cite></blockquote>
  </div>
  <div class="quote two">
    <div class="portrait b" role="img" aria-label="Portrait photo of a satisfied female customer"></div>
    <blockquote>“ Sed ut perspiciatis unde omnlois iste natus error sit volup tatem accusantium doremue laudantium, to tam rem aperiam, eaque ipsa quae ab illo inventore veritatis etuasi architecto beatae vitae dicta sunt explicaboemo enim ipsam voluptatequi”<cite>Jhon Smith, City Name</cite></blockquote>
  </div>
</section>

<section class="section newsletter">
  <span class="news-mark"></span>
  <h2>NEWSLETTER<br>SIGN UP</h2>
  <span class="news-field name">Name:</span>
  <span class="news-field email">Email Address:</span>
  <span class="btn signup">SIGN UP</span>
</section>

<section class="section reviews">
  <div class="review one">
    <h3><span class="src">Rateline</span>REVIEWS</h3>
    <p>Sed ut perspiciatis unde omnis iste natus error sioluptatem accusantium doloremque la dantium, toem aperiam, eaque ipsa quae ab illo inventorspiciatis unde omnis iste natus error sioluptatem accusantium doloremque laudantium, toem.</p>
    <div class="by"><svg width="68" height="12" viewBox="0 0 68 12"><g fill="var(--star)"><path id="st" d="M6 0l1.8 3.9 4.2.4-3.2 2.8 1 4.1L6 9.1 2.2 11.2l1-4.1L0 4.3l4.2-.4z"/><use href="#st" x="14"/><use href="#st" x="28"/><use href="#st" x="42"/><use href="#st" x="56"/></g></svg>Jhon Deo</div>
  </div>
  <div class="review two">
    <h3><span class="badge"></span><span class="src">Searchly</span>REVIEWS</h3>
    <p>Sed ut perspiciatis unde omnis iste natus error sioluptatem accusantium doloremque la dantium, toem aperiam, eaque ipsa quae ab illo inventorspiciatis unde omnis iste natus error sioluptatem accusantium doloremque laudantium, toem.</p>
    <div class="by"><svg width="68" height="12" viewBox="0 0 68 12"><g fill="var(--star)"><use href="#st"/><use href="#st" x="14"/><use href="#st" x="28"/><use href="#st" x="42"/><use href="#st" x="56"/></g></svg>Jhon Smith</div>
  </div>
</section>

<footer class="section site-footer">
  <div class="footer-top">
    <span>© 2017 Pick Our Rooftop. All Copyrights are Reserved.Terms of Use &nbsp;&nbsp; Privacy Policy &nbsp;&nbsp; Sitemap</span>
    <div class="social"><span></span><span></span><span></span><span></span><span></span></div>
  </div>
  <p class="disclaimer"><b>DISCLAIMER :</b> Sed ut perspiciatis unde omnis iste natus error sit volup ptatem accusantium doloremque laudantium, toem aperiam, eaque ipsa quae ab illo inSed ut perspiciatis unde Sed ut perspiciatis unde omnis iste natus error sioluptatem accusantium doloremque laudantium, toem aperiam, eaque ipsa quae ab illo inventore.Sed ut perspiciatis unde omnis iste natus error sioluptatem accusantium doloremque laudantium, toem aperiam, eaque ipsa quae ab illo inventore. omnis iste natus error sioluptatem accusantium doloremque l audantium, toem aperiam, eaque ipsa quae ab illo inventore.ventore.</p>
</footer>

</body>
</html>
```